Flyer-Design für Initiativbewerbung
Zielgruppe
Wir sind ein Buchhaltungsbüro. Mit diesem Flyer möchten wir uns bei Steuerberater als freier Mitarbeiter bewerben als initiativ Bewerbung! Ich lade Bilder von mir selbst mit hoch um so noch persönlicher zu werden. Die Bilder können gerne bearbeitet werden und Ausschnitte gezogen werden. Es soll sehr persönlich rüber kommen
Aufgabenstellung
Flyer sollte Din A Lang sein als Endformat, also gerne auch mehrseitig und max. 20 g haben
Sie können auch Textpassagen duplizieren und auf eine Vorderseite etc machen.
Es soll persönlich wirken obwohl es ein Werbeversand. Anbei auch das Logo unserer Firma.
Ich bin auch offen das Logo in Schwarz weiß darzustellen um so vom Blau wegzukommen.
Ich lasse mich gerne überraschen.
Text
Initiativ Bewerbung freier Mitarbeiter für Ihre Kanzlei
Sehr geehrte Damen und Herren,
gerne bewerben wir uns als freier Mitarbeiter im Rahmen des

```html
<!DOCTYPE html>
<html lang="de">
<head>
<meta charset="utf-8">
<title>Initiativbewerbung Flyer</title>
<link href="https://fonts.googleapis.com/css2?family=Barlow:wght@400;500;600&family=Barlow+Semi+Condensed:wght@500&display=swap" rel="stylesheet">
<style>
  :root {
    --blue: #0b5cb3;
    --blue-dark: #0a4fa0;
    --blue-light: #b7c3ea;
    --text: #2a2a2a;
    --paper: #ffffff;
    --bg: #ffffff;
    --photo-a: #d9d9d9;
    --photo-b: #7a7a7a;
  }
  * { margin: 0; padding: 0; box-sizing: border-box; }
  html, body { width: 1200px; height: 473px; overflow: hidden; background: var(--bg); }
  body { font-family: "Barlow", Arial, sans-serif; color: var(--text); position: relative; }

  .page {
    position: absolute; top: 27px; width: 197px; height: 418px;
    background: var(--paper);
    box-shadow: 2px 2px 5px rgba(0,0,0,0.35);
    overflow: hidden;
  }
  .page--front { left: 392px; }
  .page--letter { left: 611px; }

  .accent-bar { display: flex; height: 6px; }
  .accent-bar span { flex: 1; }
  .accent-bar .dark { background: var(--blue-dark); }
  .accent-bar .light { background: var(--blue-light); }
  .accent-bar .blank { background: var(--paper); }

  .front-head { height: 54px; text-align: center; padding-top: 15px; }
  .front-title { font-size: 11px; font-weight: 500; letter-spacing: 1.3px; color: var(--blue); }
  .front-sub { font-size: 6.4px; letter-spacing: 0.9px; margin-top: 5px; color: var(--text); }

  .portrait {
    height: 239px;
    background: linear-gradient(100deg, var(--photo-a) 0%, #a9a9a9 35%, var(--photo-b) 55%, #cfcfcf 100%);
  }

  .front-foot { background: var(--blue); height: 113px; display: flex; align-items: center; justify-content: center; gap: 6px; }
  .brand-mark { width: 10px; height: 10px; background: #fff; }
  .brand-name { color: #fff; font-size: 13px; font-weight: 400; letter-spacing: 1px; }

  .letter-body { padding: 47px 20px 0 20px; font-size: 6.5px; line-height: 12.5px; }
  .greeting { color: var(--blue-light); font-weight: 500; margin-bottom: 13px; }
  .letter-body p { margin-bottom: 13px; }
  .services {
    border: 1px solid var(--blue-light);
    padding: 3px 8px 3px 18px;
    margin: -1px 0 13px 0;
    list-style: disc;
    font-family: "Barlow Semi Condensed", Arial, sans-serif;
    font-weight: 500; letter-spacing: 0.4px;
  }
  .signature {
    width: 52px; height: 18px; margin-top: -3px;
    background: linear-gradient(90deg, rgba(11,92,179,0.25), rgba(11,92,179,0.08));
    border-radius: 2px;
  }
  .signer { color: var(--blue-light); font-size: 4.6px; font-weight: 600; line-height: 8px; }

  .letter-foot {
    position: absolute; left: 0; right: 0; bottom: 0; height: 73px;
    background: var(--blue); color: #fff; text-align: center;
    font-size: 6.5px; line-height: 12.5px; padding-top: 17px;
  }
  .letter-foot svg { vertical-align: -1px; }
</style>
</head>
<body>

<section class="page page--front">
  <div class="accent-bar"><span class="dark"></span><span class="light"></span></div>
  <header class="front-head">
    <h1 class="front-title">INITIATIV BEWERBUNG</h1>
    <p class="front-sub">freier Mitarbeiter für Ihre Kanzlei</p>
  </header>
  <div class="portrait" role="img" aria-label="Schwarz-Weiß-Porträt des Bewerbers am Schreibtisch"></div>
  <div class="accent-bar"><span class="blank"></span><span class="light"></span></div>
  <footer class="front-foot">
    <span class="brand-mark"></span>
    <span class="brand-name">KONTOWERK GmbH</span>
  </footer>
</section>

<section class="page page--letter">
  <div class="accent-bar"><span class="dark"></span><span class="light"></span></div>
  <div class="letter-body">
    <p class="greeting">Sehr geehrte Damen und Herren,</p>
    <p>gerne bewerben wir uns als freier Mitarbeiter im<br>Rahmen des § 17 BOStB für Ihre Kanzlei.</p>
    <p>Gerne übernehmen wir für Sie im Rahmen der<br>freien Mitarbeiter:</p>
    <ul class="services">
      <li>FINANZBUCHHALTUNG</li>
      <li>LOHNBUCHHALTUNG (AUCH BAULOHN)</li>
      <li>JAHRESABSCHLUSS</li>
      <li>STEUERERKLÄRUNGEN</li>
    </ul>
    <p>Fachliche Erfahrungen bestehen seit über 20<br>Jahren. Die Tätigkeit auf diversen branchenübli-<br>chen Abrechnungsprogrammen ist uns vertraut.</p>
    <p>Mit freundlichen Grüßen</p>
    <div class="signature" role="img" aria-label="Handschriftliche Unterschrift"></div>
    <div class="signer">Jonas Berger</div>
  </div>
  <footer class="letter-foot">
    Kontowerk GmbH • Lindenstraße 12<br>
    70199 Musterstadt •
    <svg width="5" height="6" viewBox="0 0 5 6"><path d="M1 0.5 Q4 3 1 5.5" stroke="#fff" stroke-width="1.1" fill="none"/></svg>
    0711/48203917<br>
    <svg width="7" height="5" viewBox="0 0 7 5"><rect x="0.3" y="0.3" width="6.4" height="4.4" fill="none" stroke="#fff" stroke-width="0.6"/><path d="M0.3 0.3 L3.5 2.8 L6.7 0.3" fill="none" stroke="#fff" stroke-width="0.6"/></svg>
    info@kontowerk-beispiel.de
  </footer>
</section>

</body>
</html>
```